Dental Patient Education Single page-Multiple pages needed.

I am creating a unique dental patient education materials for resale. I work in the dental industry, training dentists and thier teams how to improve patient acceptance rates for treatment. I see a need that all patient education material is designed incorrectly. I want to fix this by creating patient education material that educated patients based on all of the treatment options for a diagnosed condition. Tradidional patient education material reads like a catalog of procedures. This format is not effective for helping the patient quickly understand the consequences of non treatment and the benefits and disadvantages of their treatment options. Specifics of the Job:The design images must be royalty free.I will provide the text.Initially there are for major diagnosed conditions: Infected Tooth Treatment Options, Single to Multiple Missing tooth Treatment Options, Full Arch of Missing Teeth Treatment Options, and Full Arch Fixed Dental Implant Treatment OptionsThe layout should mirror the attached sample of Single Missing Tooth Treatment Options.This is a project that will require edits and redesigned based on testing.I also need this in Adobe, so it can be customized/branded for a dental office.

Target Market(s)

Dental office professionals to educate patients.

Font styles to use
Sans Serif

Colors
3277b5

Requirements
Must have
• Professional look and feel
• Royalty free images
• Easy to read

```html
<!DOCTYPE html>
<html lang="en">
<head>
<meta charset="utf-8">
<title>Single Missing Tooth – Treatment Options</title>
<link href="https://fonts.googleapis.com/css2?family=Montserrat:wght@400;500;600;800&display=swap" rel="stylesheet">
<style>
  :root {
    --brand-blue: #3277b5;
    --deep-blue: #1a6fb5;
    --soft-grey: #a9b2b8;
    --pale-grey: #dfe3e6;
    --backdrop: #e6e8ea;
    --ink: #2b2b2b;
    --paper: #ffffff;
  }
  * { box-sizing: border-box; margin: 0; padding: 0; }
  html, body { width: 1200px; height: 859px; overflow: hidden; }
  body {
    background: var(--backdrop);
    font-family: "Montserrat", Arial, sans-serif;
    color: var(--ink);
    position: relative;
  }
  .page {
    position: absolute;
    top: 62px;
    width: 519px;
    height: 734px;
    background: var(--paper);
    overflow: hidden;
  }
  .page--cover { left: 62px; }
  .page--options { left: 618px; }
  .page-art { position: absolute; inset: 0; }
  .abs { position: absolute; }

  /* Cover */
  .cover-title {
    position: absolute; left: 128px; top: 436px;
    color: var(--deep-blue);
    font-weight: 800; font-size: 44px; line-height: 45px;
    letter-spacing: 0.5px;
  }
  .cover-subtitle {
    position: absolute; left: 128px; top: 526px;
    color: var(--deep-blue); font-weight: 500; font-size: 12.6px;
  }
  .cover-intro {
    position: absolute; right: 24px; top: 597px; width: 240px;
    text-align: right; font-size: 10.2px; line-height: 12.8px; color: #333;
  }
  .cover-intro p + p { margin-top: 9px; }
  .placeholder { position: absolute; }

  /* Options */
  .option-heading {
    position: absolute;
    color: var(--deep-blue);
    font-weight: 800; font-size: 15px; line-height: 19px;
    letter-spacing: 0.3px;
  }
  .option-body {
    position: absolute; width: 205px;
    font-size: 8.3px; line-height: 10.4px; text-align: justify; color: #333;
  }
</style>
</head>
<body>

<section class="page page--cover">
  <svg class="page-art" viewBox="0 0 519 734" width="519" height="734" aria-hidden="true">
    <path d="M0 0 H90 C30 150 20 380 80 560 C110 640 170 700 230 734 H0 Z" fill="var(--soft-grey)"/>
    <path d="M90 0 H140 C70 150 60 380 125 550 C165 640 230 700 290 734 H230 C170 700 110 640 80 560 C20 380 30 150 90 0 Z" fill="var(--brand-blue)"/>
    <path d="M140 0 H150 C85 150 75 380 140 548 C180 640 240 700 300 734 H290 C230 700 165 640 125 550 C60 380 70 150 140 0 Z" fill="var(--pale-grey)"/>
    <path d="M519 390 C430 430 300 430 210 370 C130 310 110 140 160 0 H519 Z" fill="var(--brand-blue)"/>
  </svg>
  <svg class="placeholder" style="left:0;top:0" width="519" height="420" viewBox="0 0 519 420" role="img" aria-label="Close-up photo of a smiling woman's lower face and white teeth">
    <defs>
      <linearGradient id="skin" x1="0" y1="0" x2="0" y2="1">
        <stop offset="0" stop-color="#f0c7ac"/><stop offset="1" stop-color="#e4ae90"/>
      </linearGradient>
    </defs>
    <path d="M519 380 C430 418 305 415 218 358 C143 300 125 140 172 0 H519 Z" fill="url(#skin)"/>
  </svg>
  <div class="placeholder" role="img" aria-label="Illustration of a lower jaw with dental implants"
       style="left:0;top:562px;width:238px;height:172px;background:linear-gradient(135deg,#f3f3f3 0%,#e8b3b8 55%,#d98790 100%);border-top-right-radius:60px;"></div>

  <h1 class="cover-title">SINGLE<br>MISSING TOOTH</h1>
  <p class="cover-subtitle">A missing tooth is a serious issue. It can cause long-term</p>
  <div class="cover-intro">
    <p>A missing tooth is a serious issue. It can cause long-term damage to facial structure, bone density and your ability to feel confident in your smile.</p>
    <p>Brightway Dental Studio has several options available to fix your missing tooth.</p>
  </div>
</section>

<section class="page page--options">
  <svg class="page-art" viewBox="0 0 519 734" width="519" height="734" aria-hidden="true">
    <path d="M0 0 H519 V30 C420 10 250 -5 0 60 Z" fill="var(--soft-grey)"/>
    <path d="M0 60 C180 10 360 -5 519 40 V108 C470 60 360 25 250 25 C150 25 70 45 0 60 Z" fill="var(--brand-blue)"/>
    <path d="M519 560 C470 600 380 680 300 734 H519 Z" fill="var(--pale-grey)"/>
  </svg>

  <h2 class="option-heading" style="left:32px;top:62px">OPTION 1:<br>DO NOTHING</h2>
  <p class="option-body" style="left:32px;top:109px">If you choose to do nothing at this time, the cost down the road can be substantial. $10,000+ for orthodontics to straighten out the teeth, implant, abutment and crown, bone grafting and possible sinus lift to replace lost bone.</p>
  <div class="placeholder" role="img" aria-label="Dental X-ray showing a damaged tooth circled in red"
       style="left:290px;top:60px;width:128px;height:94px;background:linear-gradient(135deg,#1e2a33,#5d6b75 55%,#222c34);"></div>

  <h2 class="option-heading" style="left:289px;top:180px">OPTION 2:<br>DENTAL IMPLANT</h2>
  <p class="option-body" style="left:289px;top:223px">The bad news is that a dental implant is the most expensive option, BUT the good news is it is the most effective, functional and aesthetically pleasing. A dental implant will keep the bone in that area of the jaw from atrophy. It helps maintain face shape and prevents 'sunken face'. The implant will prevent surrounding teeth from shifting and chances of losing the tooth decline. It will keep the teeth from shifting, and will prevent any future need to cut down the adjacent teeth. A dental implant is the nearest thing to a natural tooth available today.</p>
  <div class="placeholder" role="img" aria-label="Labelled illustration of an implant, abutment and crown placed in the upper jaw"
       style="left:32px;top:226px;width:218px;height:100px;background:linear-gradient(90deg,#ffffff 0%,#f4d3d5 45%,#e9a9ae 100%);border-radius:30px 30px 10px 10px;"></div>

  <h2 class="option-heading" style="left:32px;top:376px">OPTION 3:<br>DENTAL BRIDGE</h2>
  <p class="option-body" style="left:32px;top:423px">The good news here is that a bridge is less expensive than the implant option BUT you will continue to lose bone in that area over time. Food will get caught in the hard to reach areas and if not cleaned properly could mean you have to replace the bridge every 7 years. In addition, to secure the bridge, the adjacent teeth must be cut down in order to be used as anchors for the appliance. Why cut down two good teeth if we don't have to?</p>
  <div class="placeholder" role="img" aria-label="Illustration of a three-tooth dental bridge fitting onto the upper teeth"
       style="left:289px;top:408px;width:204px;height:117px;background:linear-gradient(180deg,#e89aa1 0%,#f5dadc 40%,#ffffff 100%);border-radius:20px 20px 4px 4px;"></div>

  <div class="placeholder" role="img" aria-label="Illustration of a removable partial denture fitting onto the upper teeth"
       style="left:32px;top:544px;width:218px;height:162px;background:linear-gradient(180deg,#e89aa1 0%,#f6e0e2 45%,#e29aa1 80%,#ffffff 100%);border-radius:20px 20px 4px 4px;"></div>
  <h2 class="option-heading" style="left:289px;top:562px">OPTION 4:<br>THE REMOVABLE PARTIAL<br>DENTURE (RPO)</h2>
  <p class="option-body" style="left:289px;top:625px">The good news here is that it's the least expensive option of the 3, but the BAD news is that your teeth have to come out every night. You won't be able to chew your food as well and your tongue will be uncomfortable with the big, bulky plastic sitting in your mouth all day.</p>
</section>

</body>
</html>
```